Lighting bulbs packaging design

My company is a lighting products manufacturer. Our trademark is "quarnix". I need packaging design for 2 series of lighting bulbs.
1. HID bulbs.
2. Vintage filament bulbs. (need lighting bulb label on one side)

Industry/Entity Type

It Company

Colors

Designer to choose colors to be used in the design.

```html
<!DOCTYPE html>
<html lang="en">
<head>
<meta charset="utf-8">
<title>Quarnix Metal Halide 50w Carton Dieline</title>
<link rel="stylesheet" href="https://fonts.googleapis.com/css2?family=Arimo:wght@400;700&family=Exo+2:wght@400;600&display=swap">
<style>
  :root{
    --paper:#ffffff;
    --teal-light:#9fdbe3;
    --teal-mid:#5eaec0;
    --steel:#3b7a95;
    --steel-dark:#2f6a84;
    --facts:#4e88a3;
    --amber:#f3a81c;
    --ink:#1f2a33;
    --white:#ffffff;
    --line:#c9d4da;
  }
  *{box-sizing:border-box;margin:0;padding:0}
  html,body{width:1200px;height:1200px;overflow:hidden;background:var(--paper)}
  body{font-family:"Arimo",Arial,sans-serif;color:var(--white)}
  .dieline{position:absolute;left:0;top:0;width:650px;height:650px;transform:scale(1.8462);transform-origin:0 0}
  .panel{position:absolute;overflow:hidden;
    background:linear-gradient(to bottom,var(--paper) 0,var(--paper) 72px,var(--teal-light) 73px,var(--teal-mid) 200px,var(--steel) 305px)}
  .panel--front{left:90px;top:173px;width:116px;height:305px}
  .panel--facts{left:208px;top:173px;width:111px;height:305px;background:var(--facts)}
  .panel--back{left:328px;top:173px;width:116px;height:305px}
  .panel--side{left:446px;top:173px;width:122px;height:305px}
  .tuck-top{position:absolute;left:90px;top:48px;width:116px;height:125px;transform:rotate(180deg);overflow:hidden;
    background:linear-gradient(to bottom,var(--paper) 0,var(--paper) 50px,var(--teal-light) 51px,var(--steel) 125px)}
  .tuck-top::after{content:"";position:absolute;left:0;right:0;bottom:0;height:10px;background:var(--steel-dark)}
  .tuck-bottom{position:absolute;left:328px;top:478px;width:116px;height:132px;background:var(--steel)}
  .brand{position:absolute;left:0;right:0;top:50px;display:flex;align-items:center;justify-content:center;gap:4px;
    font-family:"Exo 2",sans-serif;font-weight:600;font-size:12px;letter-spacing:1px;color:var(--ink)}
  .brand__dot{width:9px;height:9px;border-radius:50%;background:var(--amber)}
  .bulb-art{position:absolute;left:36px;top:80px;width:44px;height:165px;border-radius:22px 22px 8px 8px;
    background:linear-gradient(to bottom,#eef6f8,#c6dde3 70%,#a9b4b8)}
  .product{position:absolute;left:0;right:0;text-align:center;font-family:"Exo 2",sans-serif;color:var(--amber)}
  .product--small{top:258px;font-size:11.5px;letter-spacing:.5px}
  .watt--small{position:absolute;left:0;right:0;top:272px;text-align:center;font-family:"Exo 2",sans-serif;font-size:13px}
  .spec-row{position:absolute;left:6px;right:6px;top:292px;display:flex;justify-content:space-between;font-size:5.5px;letter-spacing:.3px}
  .product--big{top:118px;font-size:20px;line-height:24px;letter-spacing:1px}
  .watt--big{position:absolute;left:0;right:0;top:176px;text-align:center;font-family:"Exo 2",sans-serif;font-size:18px;color:var(--amber)}
  .side-code{position:absolute;left:0;right:0;top:220px;text-align:center;font-size:6.5px}
  .side-base{position:absolute;left:0;right:0;top:236px;text-align:center;font-size:8px}
  .warning{position:absolute;left:8px;right:8px;top:266px;text-align:center;font-size:5px;line-height:6.4px}
  .facts__title{position:absolute;left:10px;top:18px;font-family:"Exo 2",sans-serif;font-size:13px}
  .facts__sub{position:absolute;right:10px;top:34px;font-size:6px}
  .facts__rule{position:absolute;left:10px;right:10px;height:2px;background:var(--white)}
  .facts__list{position:absolute;left:10px;right:10px;top:48px;font-size:5.4px;list-style:none}
  .facts__row{border-bottom:.6px solid var(--line);padding:2px 0}
  .facts__head{display:flex;justify-content:space-between;font-weight:700}
  .facts__note{padding-left:6px;line-height:6.6px}
  .energy-badge{float:right;width:14px;height:12px;background:var(--ink);border:.6px solid var(--white);margin-top:1px}
  .scale{position:relative;height:10px;margin:2px 4px}
  .scale__bar{position:absolute;left:0;right:0;top:4px;height:.8px;background:var(--white)}
  .scale__mark{position:absolute;top:1px;width:2px;height:7px;background:var(--white)}
  .mercury{font-weight:700;font-size:8px;margin-top:3px}
  .mercury-text{font-size:7.4px;line-height:8.8px}
  .facts__summary{position:absolute;left:6px;right:6px;top:254px;display:flex;justify-content:space-between;text-align:center}
  .summary__label{font-size:6px;font-weight:700}
  .summary__value{font-size:17px;font-family:"Exo 2",sans-serif;line-height:17px}
  .summary__unit{font-size:5px}
  .window{position:absolute;left:7px;top:14px;width:102px;height:60px;background:var(--white)}
  .made-in{position:absolute;left:0;right:0;top:96px;text-align:center;font-size:5px;color:var(--ink);line-height:6px}
</style>
</head>
<body>
<main class="dieline">

  <section class="tuck-top">
    <div class="brand" style="top:30px"><span class="brand__dot"></span>QUARNIX</div>
    <div class="product" style="top:66px;font-size:11.5px;letter-spacing:1px;color:var(--ink)">METAL HALIDE</div>
    <div class="product" style="top:80px;font-size:12px;color:var(--ink)">50w</div>
    <div class="spec-row" style="top:102px;color:var(--ink)"><span>MH50/ED17/U/4K</span><span>MED BASE</span></div>
  </section>

  <section class="panel panel--front">
    <div class="brand"><span class="brand__dot"></span>QUARNIX</div>
    <div class="bulb-art" role="img" aria-label="Photo of a clear ED17 metal halide bulb with medium screw base"></div>
    <div class="product product--small">METAL HALIDE</div>
    <div class="watt--small">50w</div>
    <div class="spec-row"><span>MH50/ED17/U/4K</span><span>MED BASE</span></div>
  </section>

  <section class="panel panel--facts">
    <h2 class="facts__title">Lighting Facts</h2>
    <p class="facts__sub">Per Bulb</p>
    <div class="facts__rule" style="top:43px"></div>
    <ul class="facts__list">
      <li class="facts__row"><div class="facts__head"><span>Brightness</span><span>XXX lumens</span></div></li>
      <li class="facts__row">
        <div class="facts__head"><span>Estimated Yearly<br>Energy Cost</span><span>$X.XX</span></div>
        <div class="facts__note"><span class="energy-badge"></span>Based on 3 hrs/day,<br>11¢/kWh. Cost<br>depends on rates and use</div>
      </li>
      <li class="facts__row"><div class="facts__head"><span>Life</span><span>X.X years</span></div><div class="facts__note">Based on 3 hrs/day</div></li>
      <li class="facts__row">
        <div class="facts__head"><span>Light Appearance</span></div>
        <div class="facts__note" style="display:flex;justify-content:space-between;padding-right:6px"><span>Warm</span><span>Cool</span></div>
        <div class="scale"><span class="scale__bar"></span><span class="scale__mark" style="left:0"></span><span class="scale__mark" style="left:30%"></span><span class="scale__mark" style="left:60%"></span><span class="scale__mark" style="right:0"></span></div>
        <div class="facts__note" style="padding-left:14px">XXXX K</div>
      </li>
      <li class="facts__row"><div class="facts__head"><span>Energy Used</span><span>XX watts</span></div></li>
      <li>
        <p class="mercury">Contains Mercury</p>
        <p class="mercury-text">For more on clean up and safe disposal, visit lampdisposal.example/cfl.</p>
      </li>
    </ul>
    <div class="facts__summary">
      <div><p class="summary__label">Brightness</p><p class="summary__value">XXX</p><p class="summary__unit">lumens</p></div>
      <div><p class="summary__label">Estimated<br>Energy Cost</p><p class="summary__value">$X.XX</p><p class="summary__unit">per year</p></div>
    </div>
  </section>

  <section class="panel panel--back">
    <div class="brand"><span class="brand__dot"></span>QUARNIX</div>
    <div class="bulb-art" role="img" aria-label="Photo of a clear ED17 metal halide bulb with medium screw base"></div>
    <div class="product product--small">METAL HALIDE</div>
    <div class="watt--small">50w</div>
    <div class="spec-row"><span>MH50/ED17/U/4K</span><span>MED BASE</span></div>
  </section>

  <section class="panel panel--side">
    <div class="brand"><span class="brand__dot"></span>QUARNIX</div>
    <div class="product product--big">METAL<br>HALIDE</div>
    <div class="watt--big">50w</div>
    <p class="side-code">MH50/ED17/U/4K</p>
    <p class="side-base">MED BASE</p>
    <p class="warning">DANGER: for use only in fixtures containing NLSA BALLAST M110/E<br>Do not use in standard incandescent light bulb sockets</p>
  </section>

  <section class="tuck-bottom">
    <div class="window"></div>
    <p class="made-in">MANUFACTERED<br>MADE IN P.R.C.</p>
  </section>

</main>
</body>
</html>
```